Spirit Distillery needs website design for velmorastills.example

We are a spirit distillery located in Canberra, Australia. We are just about to begin production on our products: Gin, Coffee vodka, lemon myrtle vodka, and apple and cinnamon vodka.
Velmora is Ancient Greek Mythology meaning "elixir of the Gods" so Greek mythology incorporated in the website, as well as simple and user friendly layout and functionality would be great.
Pages would include:
Welcome page with links to:
Our Products (Gin, Coffee vodka, lemon myrtle vodka, and apple and cinnamon vodka)
Events (what events the distillery is attending or holding at the distillery site)
Shop (for bottle sales)
Stockists (where the bottles are sold)
Cocktail recipe page

```html
<!DOCTYPE html>
<html lang="en">
<head>
<meta charset="utf-8">
<title>Velmora Distillery</title>
<link href="https://fonts.googleapis.com/css2?family=Crimson+Text:wght@400;600&family=Roboto:wght@300;400;500;700;900&display=swap" rel="stylesheet">
<style>
:root{
  --orange:#ff7a00;
  --orange-soft:#ffa24d;
  --ink:#222;
  --text:#444;
  --muted:#666;
  --line:#e6e6e6;
  --pale:#f3f3f1;
  --white:#fff;
  --night:#1b2a30;
}
*{margin:0;padding:0;box-sizing:border-box}
html,body{width:1200px;height:3618px;overflow:hidden;background:var(--white)}
body{font-family:'Roboto',sans-serif;color:var(--text);position:relative}
.serif{font-family:'Crimson Text',serif}
.btn{position:absolute;display:flex;align-items:center;justify-content:center;background:var(--orange);color:var(--white);font:700 13px 'Roboto',sans-serif;border-radius:24px;text-transform:uppercase;letter-spacing:.2px}

/* header */
.site-header{position:absolute;left:0;top:0;width:1200px;height:93px;background:var(--white)}
.brand{position:absolute;left:111px;top:34px;font:400 25px 'Crimson Text',serif;color:var(--ink);letter-spacing:.5px}
.nav{position:absolute;top:43px;left:510px;display:flex;gap:0;font:400 14px 'Roboto',sans-serif;color:var(--ink)}
.nav span{position:absolute;white-space:nowrap}
.nav .active{color:var(--orange)}
.nav-marker{position:absolute;left:521px;top:77px;width:0;height:0;border-left:10px solid transparent;border-right:10px solid transparent;border-bottom:16px solid var(--orange)}

/* hero */
.hero{position:absolute;left:0;top:93px;width:1200px;height:593px;background:radial-gradient(ellipse at 55% 40%,#3a5258 0%,#1f3036 55%,#121c20 100%)}
.hero-title{position:absolute;left:111px;top:195px;font:900 52px/60px 'Roboto',sans-serif;color:var(--white);letter-spacing:1px}
.hero .btn{left:111px;top:324px;width:141px;height:46px}
.social-dot{position:absolute;left:1117px;width:33px;height:33px;border:1.5px solid var(--white);border-radius:50%}
.social-dot::after{content:"";position:absolute;left:12px;top:12px;width:7px;height:7px;border-radius:50%;background:var(--white)}
.slider-arrow{position:absolute;top:519px;width:48px;height:48px;border-radius:50%;background:rgba(0,0,0,.45);display:flex;align-items:center;justify-content:center}

/* welcome */
.section-title{position:absolute;left:0;width:1200px;text-align:center;font:400 34px 'Crimson Text',serif;color:var(--ink);letter-spacing:.5px}
.title-rule{position:absolute;left:564px;width:74px;height:2px;background:var(--orange)}
.welcome-text{position:absolute;left:172px;top:854px;width:856px;text-align:center;font:400 13px/24px 'Roboto',sans-serif;color:var(--text)}

/* products */
.products{position:absolute;left:0;top:1189px;width:1200px;height:668px;background:linear-gradient(120deg,#f6f6f4 0%,#eeeeea 50%,#f5f5f2 100%)}
.product-tabs{position:absolute;top:152px;left:0;width:1200px;display:flex;justify-content:center;gap:32px;font:400 14px 'Crimson Text',serif;color:var(--ink);text-transform:uppercase}
.product-tabs .active{color:var(--orange);text-decoration:underline}
.product-card{position:absolute;top:203px;width:312px;height:363px;background:var(--white);box-shadow:0 2px 10px rgba(0,0,0,.06);overflow:hidden;text-align:center}
.bottle{position:absolute;left:126px;top:18px;width:60px;height:200px;border-radius:14px 14px 8px 8px}
.product-name{position:absolute;top:232px;width:100%;font:400 20px 'Crimson Text',serif;color:var(--ink)}
.product-price{position:absolute;top:270px;width:100%;font:400 19px 'Crimson Text',serif;color:var(--orange)}
.cart{position:absolute;left:102px;top:311px;width:108px;height:108px;border-radius:50%;background:var(--orange);box-shadow:0 0 0 5px var(--orange-soft) inset, 0 0 0 0 var(--orange)}
.cart svg{position:absolute;left:45px;top:22px}

/* events */
.events-grid{position:absolute;left:111px;top:2032px;width:978px;height:759px;border:2px solid var(--line)}
.event-photo{position:absolute;width:488px;height:379px}
.event-body{position:absolute;width:488px;height:379px;padding:0 0 0 31px}
.date-badge{position:absolute;left:31px;top:44px;width:143px;height:48px;background:var(--orange);color:var(--white);font:400 14px 'Crimson Text',serif;display:flex;align-items:center;justify-content:center;gap:7px}
.event-title{position:absolute;left:31px;top:105px;width:420px;font:300 24px/28px 'Roboto',sans-serif;color:var(--ink)}
.event-text{position:absolute;left:31px;top:185px;width:420px;font:400 13px/22px 'Roboto',sans-serif;color:var(--muted)}
.learn-more{position:absolute;left:38px;top:310px;font:700 13px 'Roboto',sans-serif;color:var(--orange);border-bottom:1.5px solid var(--orange);padding-bottom:1px}

/* quote band */
.quote-band{position:absolute;left:0;top:2972px;width:1200px;height:393px;background:linear-gradient(160deg,#3b4a24 0%,#1e2a1a 40%,#202626 70%,#33402a 100%)}
.quote-text{position:absolute;left:230px;top:100px;width:740px;text-align:center;font:400 21px/34px 'Crimson Text',serif;color:var(--white)}

/* footer */
.site-footer{position:absolute;left:0;top:3365px;width:1200px;height:253px;background:var(--white)}
.footer-brand{position:absolute;left:111px;top:80px;font:400 25px/30px 'Crimson Text',serif;color:var(--ink)}
.copyright{position:absolute;left:111px;top:168px;font:400 11px/18px 'Roboto',sans-serif;color:var(--muted)}
.footer-head{position:absolute;top:86px;font:500 13px 'Roboto',sans-serif;color:var(--orange);text-transform:uppercase}
.footer-col{position:absolute;font:400 13px/26px 'Roboto',sans-serif;color:var(--muted)}
.icon-row{display:flex;align-items:center;gap:14px}
</style>
</head>
<body>

<header class="site-header">
  <div class="brand">VELMORA DISTILLERY</div>
  <nav class="nav">
    <span class="active" style="left:0">HOME</span>
    <span style="left:70px">OUR PRODUCTS</span>
    <span style="left:205px">EVENTS</span>
    <span style="left:287px">SHOP</span>
    <span style="left:354px">STOCKISTS</span>
    <span style="left:459px">COCKTAIL RECIPE</span>
  </nav>
  <div class="nav-marker"></div>
</header>

<section class="hero" role="img" aria-label="Gin and tonic in a balloon glass with lime, blueberries and mint beside a cocktail shaker on a dark background">
  <h1 class="hero-title">VELMORA<br>DISTILLERY</h1>
  <div class="btn">Read More</div>
  <div class="social-dot" style="top:227px"></div>
  <div class="social-dot" style="top:273px"></div>
  <div class="social-dot" style="top:319px"></div>
  <div class="social-dot" style="top:365px"></div>
  <div class="slider-arrow" style="left:542px"><svg width="12" height="18" viewBox="0 0 12 18"><path d="M9 2 L3 9 L9 16" stroke="#fff" stroke-width="2" fill="none"/></svg></div>
  <div class="slider-arrow" style="left:608px"><svg width="12" height="18" viewBox="0 0 12 18"><path d="M3 2 L9 9 L3 16" stroke="#fff" stroke-width="2" fill="none"/></svg></div>
</section>

<section class="welcome">
  <h2 class="section-title" style="top:780px">WELCOME TO VELMORA DISTILLERY</h2>
  <div class="title-rule" style="top:835px"></div>
  <p class="welcome-text">Lorem ipsum dolor sit amet, consectetur adipiscing elit, sed do eiusmod tempor incididunt ut labore et dolore magna aliqua. Ut enim ad minim veniam, quis nostrud exercitation ullamco laboris nisi ut aliquip ex ea commodo consequat. Duis aute irure dolor in reprehenderit in voluptate velit esse cillum dolore eu fugiat nulla pariatur. Excepteur sint occaecat cupidatat non proident, sunt in culpa qui officia deserunt mollit anim id est laborum. Lorem ipsum dolor sit amet, consectetur adipiscing elit, sed do eiusmod tempor incididunt ut labore et dolore magna aliqua. Ut enim ad minim veniam, quis nostrud exercitation ullamco laboris nisi ut aliquip ex ea commodo consequat. Duis aute irure dolor in reprehenderit in voluptate velit esse cillum dolore eu fugiat nulla pariatur. Excepteur sint occaecat cupidatat non proident, sunt in culpa qui officia deserunt mollit anim id est laborum.</p>
  <div class="btn" style="left:530px;top:1040px;width:140px;height:46px">Read More</div>
</section>

<section class="products">
  <h2 class="section-title" style="top:93px">OUR PRODUCTS</h2>
  <div class="product-tabs">
    <span class="active">All</span><span>Gin</span><span>Coffee Vodka</span><span>Lemon Myrtle Vodka</span><span>Apple</span><span>Cinnamon Vodka</span>
  </div>

  <article class="product-card" style="left:111px">
    <div class="bottle" role="img" aria-label="Amber spirit bottle" style="background:linear-gradient(180deg,#8a5a2e 0%,#7a4a22 40%,#b88a5a 100%)"></div>
    <div class="product-name">Nemo enim ipsam</div>
    <div class="product-price">$25.00</div>
    <div class="cart"><svg width="18" height="16" viewBox="0 0 18 16"><path d="M1 1 H4 L6 10 H15 L17 4 H5" stroke="#fff" stroke-width="2" fill="#fff"/><circle cx="7" cy="14" r="1.6" fill="#fff"/><circle cx="14" cy="14" r="1.6" fill="#fff"/></svg></div>
  </article>

  <article class="product-card" style="left:444px">
    <div class="bottle" role="img" aria-label="Clear spirit bottle" style="background:linear-gradient(180deg,#d8dcdc 0%,#c9cccb 40%,#b08e66 100%)"></div>
    <div class="product-name">Nemo enim ipsam</div>
    <div class="product-price">$25.00</div>
    <div class="cart"><svg width="18" height="16" viewBox="0 0 18 16"><path d="M1 1 H4 L6 10 H15 L17 4 H5" stroke="#fff" stroke-width="2" fill="#fff"/><circle cx="7" cy="14" r="1.6" fill="#fff"/><circle cx="14" cy="14" r="1.6" fill="#fff"/></svg></div>
  </article>

  <article class="product-card" style="left:777px">
    <div class="bottle" role="img" aria-label="Pale gold spirit bottle" style="background:linear-gradient(180deg,#d9cf8a 0%,#e2d79a 40%,#b39a66 100%)"></div>
    <div class="product-name">Nemo enim ipsam</div>
    <div class="product-price">$25.00</div>
    <div class="cart"><svg width="18" height="16" viewBox="0 0 18 16"><path d="M1 1 H4 L6 10 H15 L17 4 H5" stroke="#fff" stroke-width="2" fill="#fff"/><circle cx="7" cy="14" r="1.6" fill="#fff"/><circle cx="14" cy="14" r="1.6" fill="#fff"/></svg></div>
  </article>
</section>

<section class="events">
  <h2 class="section-title" style="top:1950px">LATEST EVENTS</h2>
  <div class="events-grid">
    <div class="event-photo" role="img" aria-label="Gin cocktails with citrus, cucumber and spices on a dark wooden table" style="left:0;top:0;background:linear-gradient(150deg,#3a3a3a 0%,#262626 60%,#4a4034 100%)"></div>
    <div class="event-body" style="left:488px;top:0">
      <div class="date-badge"><svg width="12" height="12" viewBox="0 0 12 12"><rect x="1" y="2" width="10" height="9" fill="none" stroke="#fff"/><line x1="1" y1="5" x2="11" y2="5" stroke="#fff"/></svg>Jan 20,2021</div>
      <h3 class="event-title">Lorem ipsum dolor sit amet, conse ctetur adipiscing</h3>
      <p class="event-text">Lorem ipsum dolor sit amet, consectetur adipiscing elit, sed do eiusmod tempor incididunt ut labore et dolore magna aliqua. Ut enim ad minim veniam, quis nostrud exercitation ullamco laboris nisi ut aliquip ex ea commodo consequat. Duis aute irure dolor in reprehenderit in voluptate velit esse cillum dolore</p>
      <span class="learn-more">Learn more ⟶</span>
    </div>
    <div class="event-body" style="left:0;top:379px">
      <div class="date-badge"><svg width="12" height="12" viewBox="0 0 12 12"><rect x="1" y="2" width="10" height="9" fill="none" stroke="#fff"/><line x1="1" y1="5" x2="11" y2="5" stroke="#fff"/></svg>Jan 20,2021</div>
      <h3 class="event-title">Lorem ipsum dolor sit amet, conse ctetur adipiscing</h3>
      <p class="event-text">Lorem ipsum dolor sit amet, consectetur adipiscing elit, sed do eiusmod tempor incididunt ut labore et dolore magna aliqua. Ut enim ad minim veniam, quis nostrud exercitation ullamco laboris nisi ut aliquip ex ea commodo consequat. Duis aute irure dolor in reprehenderit in voluptate velit esse cillum dolore</p>
      <span class="learn-more">Learn more ⟶</span>
    </div>
    <div class="event-photo" role="img" aria-label="Gin tonic with blackberries and lime beside a bottle on a dark blue surface" style="left:488px;top:379px;background:linear-gradient(200deg,#2c3a44 0%,#1a242c 60%,#33453a 100%)"></div>
  </div>
  <div class="btn" style="left:530px;top:2825px;width:140px;height:46px">View More</div>
</section>

<section class="quote-band" role="img" aria-label="Tequila shots with salted rims and lime wedges, darkened">
  <p class="quote-text">Lorem ipsum dolor sit amet, consectetur adipiscing elit, sed do eiusmod tempor incididunt ut labore et dolore magna aliqua. Ut enim ad minim veniam, quis nostrud exercitation ullamco laboris nisi ut aliquip ex ea commodo consequat. Duis aute irure dolor in reprehenderit in voluptate velit esse cillum dolore</p>
  <div class="btn" style="left:530px;top:250px;width:140px;height:46px">View More</div>
</section>

<footer class="site-footer">
  <div class="footer-brand">VELMORA<br>DISTILLERY</div>
  <div class="copyright">Copyright 2021 Velmora Stills<br>All Right Reserved</div>

  <div class="footer-head" style="left:403px">Site Map</div>
  <div class="footer-col" style="left:403px;top:106px">Home<br>About Us<br>Events<br>Gallery</div>
  <div class="footer-col" style="left:496px;top:106px">Reviews<br>Blog<br>Contact Us</div>

  <div class="footer-head" style="left:669px">Contact Info</div>
  <div class="footer-col" style="left:669px;top:106px">
    Lorem ipsum dolor sit amet, consec<br>tetur adipiscing
    <div class="icon-row"><svg width="12" height="12" viewBox="0 0 12 12"><path d="M2 1 L4.5 1 L5.5 4 L4 5 Q5.5 8 7.5 8.5 L8.5 7 L11 8 L11 10.5 Q5 11 1.5 3 Z" fill="#ff7a00"/></svg>+61 2 5550 1234</div>
    <div class="icon-row"><svg width="12" height="10" viewBox="0 0 12 10"><rect width="12" height="10" fill="#ff7a00"/><path d="M0 0 L6 5 L12 0" stroke="#fff" fill="none"/></svg>hello@velmorastills.example</div>
  </div>

  <div class="footer-head" style="left:995px">Follow Us</div>
  <div class="footer-col" style="left:999px;top:110px;line-height:34px">
    <div class="icon-row"><svg width="8" height="8"><circle cx="4" cy="4" r="4" fill="#ff7a00"/></svg>Friendwall</div>
    <div class="icon-row"><svg width="8" height="8"><circle cx="4" cy="4" r="4" fill="#ff7a00"/></svg>Chirper</div>
    <div class="icon-row"><svg width="8" height="8"><circle cx="4" cy="4" r="4" fill="#ff7a00"/></svg>WorkLink</div>
  </div>
</footer>

</body>
</html>
```